Garden Design Flier

I would like a PDF of this half page A4 flier in soft green tones with dark green leaves.

Target Market(s)

Home owners and real estate agents

Font styles to use
Serif
Other font styles liked:
• Papyrus

Colors
acd136
9bcb3c
cadf82
fefdec

Requirements
Must have
• Green tones
Nice to have
• Leaves, vines, lawns
Should not have
• Open to ideas, but classic style

```html
<!DOCTYPE html>
<html lang="en">
<head>
<meta charset="utf-8">
<title>Hedgerow Gardens – Flier</title>
<link rel="stylesheet" href="https://fonts.googleapis.com/css2?family=Open+Sans:wght@400;700;800&display=swap">
<style>
  :root{
    --backdrop:#414042;
    --cream:#fcfce6;
    --lime-top:#8cc63f;
    --lime-mid:#acd136;
    --lime-glow:#d7e021;
    --vine:#66a640;
    --leaf-dark:#2e6b33;
    --leaf-mid:#4f9e45;
    --teal:#12b5a3;
    --ink:#231f20;
    --khaki:#c2c296;
  }
  *{margin:0;padding:0;box-sizing:border-box}
  html,body{width:1200px;height:1200px;overflow:hidden;background:var(--backdrop)}
  body{font-family:"Open Sans",Arial,sans-serif;color:var(--ink)}
  .flier{position:absolute;left:215px;top:55px;width:770px;height:1089px;background:var(--cream);overflow:hidden}
  .header-art{position:absolute;left:0;top:0;width:770px;height:520px}
  .brand{position:absolute;left:0;width:428px;text-align:center}
  .brand-mark{position:absolute;left:189px;top:345px;width:50px;height:50px;border-radius:50%;background:var(--teal)}
  .brand-name{top:412px;font-weight:800;color:var(--teal);font-size:48px;line-height:54px;letter-spacing:1px}
  .owner{top:538px;font-size:22px;line-height:30px}
  .credential{top:584px;font-size:13px;line-height:18px}
  .intro{position:absolute;left:79px;top:655px;width:320px;font-size:21px;line-height:33px;white-space:nowrap}
  .motto{position:absolute;left:0;top:0;width:770px;height:1089px;pointer-events:none}
  .motto text{font-family:"Open Sans",Arial,sans-serif;font-weight:800;fill:var(--khaki);text-anchor:end}
  .contact{position:absolute;top:1000px;text-align:center;font-size:14px;color:#3a3a3a}
  .contact-icon{display:block;margin:0 auto 10px;width:30px;height:30px}
  .abn-label{display:block;font-weight:700;color:var(--teal);font-size:20px;line-height:22px;margin:8px 0 6px}
</style>
</head>
<body>
<main class="flier">
  <svg class="header-art" viewBox="0 0 770 520" role="img" aria-label="Illustration of dark green leaves on a curling vine across a lime-green sky">
    <defs>
      <linearGradient id="sky" x1="0" y1="0" x2="0" y2="1">
        <stop offset="0" stop-color="var(--lime-top)"/>
        <stop offset="0.7" stop-color="var(--lime-mid)"/>
        <stop offset="1" stop-color="var(--lime-glow)"/>
      </linearGradient>
      <linearGradient id="foliage" x1="0" y1="0" x2="1" y2="0.3">
        <stop offset="0.3" stop-color="var(--leaf-mid)" stop-opacity="0"/>
        <stop offset="0.7" stop-color="var(--leaf-mid)" stop-opacity="0.55"/>
        <stop offset="1" stop-color="var(--leaf-dark)" stop-opacity="0.85"/>
      </linearGradient>
    </defs>
    <path d="M0 0H770V400C640 390 530 345 430 305C300 255 130 240 0 300Z" fill="url(#sky)"/>
    <path d="M0 0H770V400C640 390 530 345 430 305C300 255 130 240 0 300Z" fill="url(#foliage)"/>
    <path d="M0 292C120 245 260 228 400 262C520 292 640 370 770 440" fill="none" stroke="var(--vine)" stroke-width="13"/>
    <path d="M520 318C600 360 680 420 770 455" fill="none" stroke="var(--vine)" stroke-width="3"/>
  </svg>

  <span class="brand-mark" aria-hidden="true"></span>
  <h1 class="brand brand-name">HEDGEROW<br>GARDENS</h1>
  <p class="brand owner">by Liam Carver</p>
  <p class="brand credential">Certificate III. Horticulture, Riverbend Institute</p>

  <p class="intro">All your gardening and land-<br>scaping needs from<br>design and installation to<br>general maintenance<br>Bespoke vegetables gardens<br>and potager designs<br>created to suite your site<br>and requirements.</p>

  <svg class="motto" viewBox="0 0 770 1089" aria-label="Design, install, grow, tend, enjoy">
    <text x="692" y="570" font-size="40" textLength="144" lengthAdjust="spacingAndGlyphs">DESIGN</text>
    <text x="692" y="636" font-size="63" textLength="251" lengthAdjust="spacingAndGlyphs">INSTALL</text>
    <text x="692" y="710" font-size="80" textLength="251" lengthAdjust="spacingAndGlyphs">GROW</text>
    <text x="692" y="798" font-size="95" textLength="251" lengthAdjust="spacingAndGlyphs">TEND</text>
    <text x="692" y="870" font-size="78" textLength="251" lengthAdjust="spacingAndGlyphs">ENJOY</text>
  </svg>

  <div class="contact" style="left:77px;width:200px">
    <svg class="contact-icon" viewBox="0 0 30 30" aria-hidden="true">
      <circle cx="15" cy="15" r="15" fill="var(--teal)"/>
      <rect x="7" y="9.5" width="16" height="11" fill="none" stroke="#fff" stroke-width="1.6"/>
      <path d="M7 9.5L15 16L23 9.5M7 20.5L12.5 15M23 20.5L17.5 15" fill="none" stroke="#fff" stroke-width="1.6"/>
    </svg>
    liam@hedgerowgardens.com.au
  </div>
  <div class="contact" style="left:291px;width:120px">
    <svg class="contact-icon" viewBox="0 0 30 30" aria-hidden="true">
      <circle cx="15" cy="15" r="15" fill="var(--teal)"/>
      <circle cx="15" cy="15" r="9" fill="none" stroke="#fff" stroke-width="1.6"/>
      <path d="M11.5 17.5c1.5 1.5 3 2 4 1.6l1.3-1.2-1.6-1.6-1 .8c-.8-.4-1.5-1.1-1.9-1.9l.8-1-1.6-1.6-1.2 1.3c-.4 1 .1 2.5 1.2 4.2z" fill="#fff"/>
    </svg>
    0400-318275
  </div>
  <div class="contact" style="left:437px;width:120px">
    <span class="abn-label">ABN</span>
    51902736418
  </div>
</main>
</body>
</html>
```